Silver Heron Martial Arts Banner & poster design

We need a 6' wide x 4' high banner and a stand up poster 32" w x 80" h designed for our upcoming International Black Belt Grading. We are attaching our logo and a few designs that we like, and also would like to exceed the designs. We can send an additional photo of our Grandmaster to include on the stand up poster if requested.

Colors
6b449b
ffc214
ffffff
b2b2b2
474747
1b1b1b

Requirements
Must have
• Logo; and the wording: Train Harder than the Rest; because You Train with the Best.

```html
<!DOCTYPE html>
<html lang="en">
<head>
<meta charset="utf-8">
<title>Silver Heron Martial Arts – Stand Up Poster</title>
<link rel="stylesheet" href="https://fonts.googleapis.com/css2?family=Anton&display=swap">
<style>
  :root {
    --purple: #6b449b;
    --gold: #ffc214;
    --white: #ffffff;
    --silver: #b2b2b2;
    --charcoal: #474747;
    --ink: #1b1b1b;
  }
  html, body {
    margin: 0;
    padding: 0;
    width: 1200px;
    height: 2963px;
    overflow: hidden;
    background: var(--white);
  }
  .poster {
    position: relative;
    width: 1200px;
    height: 2963px;
    overflow: hidden;
    background: var(--purple);
  }
  .poster__waves {
    position: absolute;
    inset: 0;
  }
  .brand-mark {
    position: absolute;
    left: 649px;
    top: 41px;
    width: 453px;
    height: 500px;
    background: var(--white);
    display: flex;
    align-items: center;
    justify-content: center;
    flex-direction: column;
    gap: 30px;
  }
  .brand-mark__dot {
    width: 90px;
    height: 90px;
    border-radius: 50%;
    background: var(--purple);
  }
  .brand-mark__name {
    font-family: "Anton", "Impact", sans-serif;
    font-size: 64px;
    line-height: 1.1;
    color: var(--purple);
    text-align: center;
    text-transform: uppercase;
  }
  .athlete-photo {
    position: absolute;
    left: 540px;
    top: 720px;
    width: 660px;
    height: 2040px;
    background: linear-gradient(180deg, #f4f4f4 0%, #e6e6e6 55%, #f2f2f2 100%);
  }
  .belt-photo {
    position: absolute;
    left: 60px;
    top: 2630px;
    width: 450px;
    height: 230px;
    background: linear-gradient(180deg, #2a2a2a 0%, var(--ink) 100%);
    border-radius: 20px;
    opacity: .9;
  }
  .slogan {
    position: absolute;
    inset: 0;
    margin: 0;
    font-family: "Anton", "Impact", sans-serif;
    font-weight: 400;
    font-size: 150px;
    line-height: 1;
    color: var(--ink);
    pointer-events: none;
  }
  .slogan__line {
    position: absolute;
    white-space: nowrap;
    transform: scaleX(.51);
    transform-origin: 0 0;
  }
  .slogan__line--1 { left: 92px;  top: 930px; }
  .slogan__line--2 { left: 78px;  top: 1181px; }
  .slogan__line--3 { left: 98px;  top: 1473px; }
  .slogan__line--4 { left: 118px; top: 1732px; }
  .slogan__line--5 { left: 153px; top: 1993px; }
</style>
</head>
<body>
<main class="poster">
  <svg class="poster__waves" width="1200" height="2963" viewBox="0 0 1200 2963" aria-hidden="true">
    <path d="M0 560 C300 520 600 560 860 720 C1000 810 1120 930 1200 1000 L1200 2800 C1000 2760 700 2660 420 2480 C250 2370 100 2290 0 2240 Z" fill="var(--gold)"/>
    <path d="M0 595 C300 570 600 610 850 760 C990 845 1110 960 1200 1040 L1200 2760 C1000 2720 700 2620 420 2440 C250 2330 100 2255 0 2205 Z" fill="var(--white)"/>
  </svg>

  <div class="brand-mark">
    <span class="brand-mark__dot"></span>
    <span class="brand-mark__name">Silver Heron<br>Martial Arts</span>
  </div>

  <div class="athlete-photo" role="img" aria-label="Photo of a black belt martial artist in a white gi, standing and holding his belt"></div>

  <h1 class="slogan">
    <span class="slogan__line slogan__line--1">Train harder</span>
    <span class="slogan__line slogan__line--2">than the rest ,</span>
    <span class="slogan__line slogan__line--3">because you</span>
    <span class="slogan__line slogan__line--4">train with</span>
    <span class="slogan__line slogan__line--5">the best</span>
  </h1>

  <div class="belt-photo" role="img" aria-label="Photo of hands tying a black belt"></div>
</main>
</body>
</html>
```